Make the invisible visible.... and attractive

I have an online course at http://www.brightlanepath.com/Begin-today-here.html. I need an attractive graphic to sell the product. The course is a series of video, audio and handout materials set out in 32 lessons and has a free one year confidence course as a bonus.

Target Market(s)

Individuals who have problems with fear or anxiety.

Industry/Entity Type

Audio

```html
<!DOCTYPE html>
<html lang="en">
<head>
<meta charset="utf-8">
<title>The Brave Course</title>
<link rel="stylesheet" href="https://fonts.googleapis.com/css2?family=Open+Sans:wght@300;400;600;700&display=swap">
<style>
  :root {
    --page: #ffffff;
    --panel-light: #f7f7f8;
    --panel-dark: #d9dadc;
    --panel-edge: #8c8c8c;
    --title-blue: #2e3f95;
    --ink: #1f1f1f;
    --leaf: #7d9a3b;
    --leaf-ring: #7f9c3e;
    --rule: #ffffff;
    --badge: #8ba5ba;
    --figure-dark: #1c1c1c;
    --figure-mid: #4a4a4a;
  }
  * { margin: 0; padding: 0; box-sizing: border-box; }
  html, body { width: 1200px; height: 1000px; overflow: hidden; background: var(--page); }
  body { position: relative; font-family: "Open Sans", Arial, sans-serif; color: var(--ink); }

  .promo-panel {
    position: absolute; left: 207px; top: 58px; width: 791px; height: 907px;
    border: 1px solid var(--panel-edge);
    background: linear-gradient(135deg, var(--panel-light) 0%, #ececed 55%, var(--panel-dark) 100%);
  }
  .promo-panel > * { position: absolute; }

  .course-title {
    left: 0; width: 100%; top: 14px; text-align: center;
    font-size: 90px; font-weight: 300; color: var(--title-blue); letter-spacing: -2px; white-space: nowrap;
  }
  .course-title strong { font-weight: 700; }

  .divider { left: 32px; width: 740px; border-top: 2px dashed var(--rule); }
  .divider--top { top: 145px; }
  .divider--mid { top: 518px; left: 22px; width: 750px; }
  .divider--low { top: 723px; left: 22px; width: 740px; }

  .transform-line { font-size: 62px; font-weight: 300; line-height: 1; white-space: nowrap; }
  .transform-from { left: 28px; top: 172px; }
  .transform-this { left: 115px; top: 245px; }
  .transform-to { left: 51px; top: 421px; }

  .figure-area {
    border-radius: 6px;
    background: linear-gradient(160deg, var(--figure-mid) 0%, var(--figure-dark) 100%);
  }
  .figure-before { left: 273px; top: 207px; width: 108px; height: 95px; }
  .figure-after { left: 262px; top: 322px; width: 108px; height: 152px; }

  .lesson-count { left: 452px; top: 158px; width: 236px; height: 330px; text-align: center; }
  .lesson-count__lead { display: block; font-size: 28px; font-weight: 300; }
  .lesson-count__ring { position: absolute; left: 3px; top: 42px; }
  .lesson-count__number {
    position: absolute; left: 0; width: 100%; top: 80px;
    font-size: 150px; font-weight: 600; line-height: 1; letter-spacing: -4px;
  }
  .lesson-count__unit { position: absolute; left: 0; width: 100%; top: 258px; font-size: 62px; font-weight: 300; line-height: 1; }

  .format-list { left: 44px; top: 557px; display: flex; gap: 29px; list-style: none; }
  .format-item { width: 93px; text-align: center; }
  .format-item__tile {
    width: 93px; height: 93px; border-radius: 8px; background: var(--leaf);
    display: flex; align-items: center; justify-content: center;
  }
  .format-item__label { display: block; margin-top: 22px; font-size: 15px; font-weight: 400; white-space: nowrap; margin-left: -20px; margin-right: -20px; }

  .bonus-free { left: 25px; top: 770px; font-size: 86px; font-weight: 700; line-height: 1; }
  .bonus-text { left: 259px; top: 756px; font-size: 53px; font-weight: 300; line-height: 62px; white-space: nowrap; }
  .bonus-badge { left: 618px; top: 738px; }
</style>
</head>
<body>
  <main class="promo-panel">
    <h1 class="course-title">The <strong>Brave</strong> Course</h1>
    <div class="divider divider--top"></div>

    <p class="transform-line transform-from">Go from</p>
    <p class="transform-line transform-this">this...</p>
    <p class="transform-line transform-to">to this...</p>

    <div class="figure-area figure-before" role="img" aria-label="Silhouette of a person sitting hunched, hugging their knees"></div>
    <div class="figure-area figure-after" role="img" aria-label="Silhouette of a person standing with arms raised in triumph"></div>

    <div class="lesson-count">
      <span class="lesson-count__lead">in just</span>
      <svg class="lesson-count__ring" width="230" height="230" viewBox="0 0 230 230" aria-hidden="true">
        <circle cx="115" cy="115" r="108" fill="none" stroke="var(--leaf-ring)" stroke-width="4"/>
        <circle cx="116" cy="114" r="105" fill="none" stroke="var(--leaf-ring)" stroke-width="1.5" stroke-dasharray="30 14 60 20" opacity="0.7"/>
      </svg>
      <span class="lesson-count__number">29</span>
      <span class="lesson-count__unit">lessons</span>
    </div>

    <div class="divider divider--mid"></div>

    <ul class="format-list">
      <li class="format-item">
        <div class="format-item__tile">
          <svg width="66" height="60" viewBox="0 0 66 60" aria-hidden="true">
            <rect x="4" y="6" width="42" height="26" fill="var(--ink)"/>
            <path d="M46 12 L60 6 L60 32 L46 26Z" fill="var(--ink)"/>
            <path d="M20 13 L31 19 L20 25Z" fill="var(--leaf)"/>
            <path d="M25 32 L10 56 M25 32 L40 56 M25 32 L25 40" stroke="var(--ink)" stroke-width="5"/>
          </svg>
        </div>
        <span class="format-item__label">VIDEO</span>
      </li>
      <li class="format-item">
        <div class="format-item__tile">
          <svg width="66" height="56" viewBox="0 0 66 56" aria-hidden="true">
            <path d="M6 18 H18 L36 4 V52 L18 38 H6Z" fill="var(--ink)"/>
            <path d="M44 18 Q50 28 44 38 M50 12 Q60 28 50 44 M56 6 Q70 28 56 50" fill="none" stroke="var(--ink)" stroke-width="4"/>
          </svg>
        </div>
        <span class="format-item__label">AUDIO</span>
      </li>
      <li class="format-item">
        <div class="format-item__tile">
          <svg width="64" height="70" viewBox="0 0 64 70" aria-hidden="true">
            <g fill="var(--leaf)" stroke="var(--ink)" stroke-width="3">
              <rect x="26" y="3" width="34" height="42"/>
              <rect x="15" y="13" width="34" height="42"/>
              <rect x="4" y="24" width="34" height="42"/>
            </g>
            <path d="M10 34 H32 M10 40 H32 M10 46 H32 M10 52 H32 M10 58 H32" stroke="var(--ink)" stroke-width="2.5"/>
          </svg>
        </div>
        <span class="format-item__label">HANDOUTS</span>
      </li>
      <li class="format-item">
        <div class="format-item__tile">
          <svg width="66" height="66" viewBox="0 0 66 66" aria-hidden="true">
            <path d="M10 14 L50 56" stroke="var(--ink)" stroke-width="8" stroke-linecap="round"/>
            <circle cx="10" cy="12" r="9" fill="var(--ink)"/>
            <path d="M4 6 L10 12" stroke="var(--leaf)" stroke-width="5"/>
            <path d="M20 52 L52 18" stroke="var(--ink)" stroke-width="7" stroke-linecap="round"/>
            <path d="M40 6 L62 20 L56 28 L36 14Z" fill="var(--ink)"/>
          </svg>
        </div>
        <span class="format-item__label">TOOLS</span>
      </li>
      <li class="format-item">
        <div class="format-item__tile">
          <svg width="70" height="56" viewBox="0 0 70 56" aria-hidden="true">
            <ellipse cx="44" cy="20" rx="22" ry="15" fill="var(--ink)"/>
            <path d="M54 32 L62 44 L44 34Z" fill="var(--ink)"/>
            <ellipse cx="24" cy="32" rx="21" ry="14" fill="var(--ink)" stroke="var(--leaf)" stroke-width="3"/>
            <path d="M12 42 L6 54 L22 45Z" fill="var(--ink)"/>
          </svg>
        </div>
        <span class="format-item__label">DISCUSSIONS</span>
      </li>
      <li class="format-item">
        <div class="format-item__tile">
          <svg width="66" height="52" viewBox="0 0 66 52" aria-hidden="true">
            <rect x="3" y="3" width="60" height="46" fill="none" stroke="var(--ink)" stroke-width="4"/>
            <path d="M33 3 V49" stroke="var(--ink)" stroke-width="3"/>
            <path d="M9 12 H27 M9 19 H27 M9 26 H27 M9 33 H27 M9 40 H27 M39 33 H57 M39 40 H57" stroke="var(--ink)" stroke-width="2.5"/>
            <rect x="39" y="10" width="18" height="16" fill="none" stroke="var(--ink)" stroke-width="2.5"/>
          </svg>
        </div>
        <span class="format-item__label">WORKBOOK</span>
      </li>
    </ul>

    <div class="divider divider--low"></div>

    <p class="bonus-free">FREE</p>
    <p class="bonus-text">one year email<br>confidence course</p>
    <svg class="bonus-badge" width="160" height="96" viewBox="0 0 160 96" aria-label="Bonus">
      <g transform="rotate(12 80 48)">
        <polygon fill="var(--badge)" stroke="#ffffff" stroke-width="2"
          points="12,30 30,28 28,12 50,22 62,6 76,20 94,8 104,24 124,14 128,32 150,34 138,48 152,62 130,66 134,84 112,76 100,92 86,78 68,90 58,74 38,82 36,66 14,66 24,50 8,42 24,38"/>
        <text x="80" y="58" text-anchor="middle" font-family="Open Sans, Arial, sans-serif" font-size="26" font-weight="600" fill="#ffffff">BONUS</text>
      </g>
    </svg>
  </main>
</body>
</html>
```